Transform Your Giving

I need a tri-fold brochure that will fit in a standard number 10 business envelope. Harborline and Caring Works is a charitable nonprofit. The goal of this brochure is to stimulate people into thinking about other ways to make a donation. The design should communicate the essential information on donation options, create a sense of professional integrity, be graphically sharp, easy to read and laid out in a way that doesn't make the material appear crowded.

```html
<!DOCTYPE html>
<html lang="en">
<head>
<meta charset="utf-8">
<title>Transform Your Giving – Harborline and Caring Works</title>
<link href="https://fonts.googleapis.com/css2?family=Montserrat:ital,wght@0,300;0,400;0,500;0,600;0,700;0,800;1,400&display=swap" rel="stylesheet">
<style>
:root{
  --navy:#2b2a6e;
  --navy-deep:#232260;
  --green:#4cb848;
  --green-dark:#3fa23c;
  --paper:#ffffff;
  --panel:#ecebef;
  --backdrop:#ababab;
  --ink:#333;
}
*{margin:0;padding:0;box-sizing:border-box}
html,body{width:1200px;height:1200px;overflow:hidden;background:var(--backdrop)}
body{font-family:"Montserrat",sans-serif;color:var(--ink)}
.stage{position:absolute;left:0;top:0;width:1932px;height:1932px;transform:scale(0.62112);transform-origin:0 0}
.abs{position:absolute}
.sheet{position:absolute;left:412px;width:1077px;overflow:hidden}
.sheet--outside{top:78px;height:838px;background:var(--paper)}
.sheet--inside{top:988px;height:838px;background:var(--panel)}

/* outside: impact panel */
.impact-title{left:0;top:32px;width:353px;text-align:center;font-weight:800;font-size:27px;line-height:32px;color:var(--navy)}
.impact-title span{color:var(--green)}
.impact-copy{left:22px;top:110px;width:309px;text-align:center;font-size:15.5px;line-height:19px;font-weight:400;letter-spacing:-.15px}
.option-list{left:71px;top:267px;width:215px;list-style:none}
.option-list li{height:27px;margin-bottom:7.5px;border:1.5px solid var(--green);display:flex;align-items:center;justify-content:center;gap:5px;font-size:15.5px;color:#444;white-space:nowrap;letter-spacing:-.1px}
.option-list svg{width:14px;height:14px}
.photo-couple{left:0;top:490px;width:353px;height:348px}

/* outside: contact panel */
.contact-panel{left:353px;top:0;width:354px;height:838px;background:var(--green);color:#fff}
.wordmark-light{left:0;top:42px;width:354px;text-align:center}
.wordmark-light .name{font-weight:800;font-size:44px;letter-spacing:1px;color:#fff;display:inline-flex;align-items:center;gap:10px}
.wordmark-light .dot{width:14px;height:14px;border-radius:50%;background:#fff;display:inline-block}
.wordmark-light .sub{font-weight:700;font-size:8px;margin-top:4px}
.contact-intro{left:20px;top:141px;width:314px;text-align:center;font-size:15px;line-height:19.2px;font-weight:500;letter-spacing:-.1px}
.quote-box{left:55px;top:310px;width:256px;height:78px;border:1.5px solid #fff;border-radius:8px;text-align:center;padding-top:13px}
.quote-box p{font-style:italic;font-size:12px;line-height:16px}
.quote-box b{display:block;font-size:12px;margin-top:4px}
.quote-mark{left:146px;top:288px;width:64px;height:30px;background:var(--green);text-align:center;font-size:54px;font-weight:800;line-height:52px}
.will-note{left:0;top:402px;width:354px;text-align:center;line-height:20px}
.will-note .small{font-size:13.5px;font-weight:500}
.will-note .big{font-size:20px;font-weight:800;line-height:24px;white-space:nowrap}
.will-note .light{font-size:13px;font-weight:300}
.will-note .strong{font-size:15px;font-weight:800}
.contact-pill{left:99px;top:503px;width:159px;height:27px;border-radius:14px;background:var(--navy);text-align:center;font-weight:800;font-size:17px;line-height:27px;letter-spacing:.5px}
.questions{left:0;top:540px;width:354px;text-align:center}
.questions h3{font-size:20px;font-weight:800}
.questions p{font-size:15px;line-height:18px;font-weight:400}
.contact-row{left:94px;width:256px;display:flex;align-items:center;gap:9px;font-size:13.5px;line-height:16px;white-space:nowrap}
.contact-row .ring{width:31px;height:31px;border:1.3px solid #fff;border-radius:50%;display:flex;align-items:center;justify-content:center;flex:none}
.contact-row b{font-weight:700}
.follow{left:0;top:750px;width:354px;text-align:center;font-size:13.5px;font-weight:500;display:flex;justify-content:center;align-items:center;gap:8px}
.follow i{width:20px;height:20px;border-radius:50%;background:#fff;display:inline-block}
.fineprint{left:38px;top:784px;width:290px;text-align:center;font-size:5.6px;line-height:7.5px}

/* outside: cover */
.cover{left:707px;top:0;width:370px;height:838px}
.cover-text{left:0;top:344px;width:370px;text-align:center;color:#fff}
.cover-kicker{font-size:21px;font-weight:400}
.cover-line{font-size:36px;font-weight:800;display:flex;align-items:center;justify-content:center;gap:10px;margin-top:4px}
.cover-line .accent{color:var(--green)}
.cover-line svg{width:34px;height:34px}
.cover-tag{font-size:14px;font-style:italic;line-height:18px;margin-top:18px}
.method-row{left:14px;top:546px;width:350px;display:flex;justify-content:space-between;color:#fff}
.method{width:60px;text-align:center;font-size:9.5px;font-weight:700;line-height:12px}
.method .ring{width:56px;height:56px;border:1.5px solid var(--green);border-radius:50%;margin:0 auto 5px;display:flex;align-items:center;justify-content:center}
.method svg{width:30px;height:30px}
.wordmark-dark{left:0;top:705px;width:370px;text-align:center}
.wordmark-dark .name{font-size:44px;font-weight:800;color:var(--navy);display:inline-flex;align-items:center;gap:10px}
.wordmark-dark .dot{width:14px;height:14px;border-radius:50%;background:var(--navy);display:inline-block}
.wordmark-dark .sub{font-size:9.5px;font-weight:700;color:var(--navy);margin-top:6px}

/* inside */
.fold{top:0;width:1px;height:838px;background:rgba(0,0,0,.06)}
.hero-photo{left:0;top:0;width:1077px;height:240px}
.title-badge{left:29px;top:36px;width:284px;height:98px;border-radius:49px;background:var(--navy);color:#fff;display:flex;align-items:center;padding-left:30px;gap:6px}
.title-badge .num{font-size:84px;font-weight:800;color:var(--green);line-height:1}
.title-badge .words{font-size:23px;font-weight:800;line-height:22px;white-space:nowrap;letter-spacing:-.3px}
.column{position:absolute}
.way{position:relative}
.way + .way{margin-top:20px}
.way .icon{position:absolute;width:90px;height:90px;border-radius:50%;background:var(--navy);display:flex;align-items:center;justify-content:center}
.way .icon svg{width:52px;height:52px}
.way .head{margin-left:100px;min-height:96px}
.way h2{font-size:20.5px;line-height:25px;font-weight:700;color:var(--navy);letter-spacing:-.2px}
.way .lead{font-size:14px;line-height:17.5px;font-weight:700;color:var(--green);margin-top:7px;letter-spacing:-.1px}
.body-copy{font-size:14px;line-height:17.5px;font-weight:400;color:#333;letter-spacing:-.15px}
.how{display:inline-block;background:var(--green);color:#fff;font-size:15px;font-weight:500;padding:2px 11px;border-radius:3px 3px 3px 0;margin:13px 0 14px}
.ticks{list-style:none}
.ticks li{position:relative;padding-left:24px;margin-bottom:17px}
.ticks svg{position:absolute;left:0;top:2px;width:16px;height:16px}
</style>
</head>
<body>
<div class="stage">

  <!-- ============ OUTSIDE ============ -->
  <section class="sheet sheet--outside">

    <h2 class="abs impact-title">THE IMPACT OF<br><span>YOUR GIFT</span></h2>
    <p class="abs impact-copy">Your generosity drives our mission. With every Strategic and Smart gift, your generosity reaches further and drives our mission. Join our community and begin your Strategic and Smart Giving with us today.</p>
    <ul class="abs option-list">
      <li><svg viewBox="0 0 16 16"><circle cx="8" cy="8" r="6.5" fill="none" stroke="#4cb848" stroke-width="1.4"/><path d="M5 8.2l2 2 4-4.2" fill="none" stroke="#4cb848" stroke-width="1.4"/></svg>Stocks and Securities</li>
      <li><svg viewBox="0 0 16 16"><circle cx="8" cy="8" r="6.5" fill="none" stroke="#4cb848" stroke-width="1.4"/><path d="M5 8.2l2 2 4-4.2" fill="none" stroke="#4cb848" stroke-width="1.4"/></svg>DAFs</li>
      <li><svg viewBox="0 0 16 16"><circle cx="8" cy="8" r="6.5" fill="none" stroke="#4cb848" stroke-width="1.4"/><path d="M5 8.2l2 2 4-4.2" fill="none" stroke="#4cb848" stroke-width="1.4"/></svg>QCDs</li>
      <li><svg viewBox="0 0 16 16"><circle cx="8" cy="8" r="6.5" fill="none" stroke="#4cb848" stroke-width="1.4"/><path d="M5 8.2l2 2 4-4.2" fill="none" stroke="#4cb848" stroke-width="1.4"/></svg>Crypto</li>
      <li><svg viewBox="0 0 16 16"><circle cx="8" cy="8" r="6.5" fill="none" stroke="#4cb848" stroke-width="1.4"/><path d="M5 8.2l2 2 4-4.2" fill="none" stroke="#4cb848" stroke-width="1.4"/></svg>Charitable Annuity</li>
    </ul>
    <svg class="abs photo-couple" viewBox="0 0 353 348" role="img" aria-label="Photo of a smiling senior couple outdoors at sunset, looking at a map together">
      <defs><linearGradient id="sunset" x1="0" y1="0" x2="1" y2="1"><stop offset="0" stop-color="#f2b65a"/><stop offset=".45" stop-color="#9a5a33"/><stop offset="1" stop-color="#4a3424"/></linearGradient></defs>
      <path d="M0 32 Q176 -20 353 32 V348 H0Z" fill="url(#sunset)"/>
      <path d="M0 34 Q176 -14 353 34 Q176 -4 0 60Z" fill="#4cb848"/>
    </svg>

    <div class="abs contact-panel">
      <div class="abs wordmark-light"><div class="name"><span class="dot"></span>Harborline</div><div class="sub">HARBORLINE AND CARING WORKS, INC.</div></div>
      <p class="abs contact-intro">To learn more about Smart Giving Options and how they can benefit you and Harborline and Caring Works, please reach out to our team. We're here to help you navigate these giving methods and answer any question you may have.</p>
      <div class="abs quote-box"><p>Being kind to others is a way of being<br>good to yourself.</p><b>Harlan Kessler</b></div>
      <div class="abs quote-mark">&ldquo;</div>
      <div class="abs will-note">
        <div class="small">If you do not have a will</div>
        <div class="big">go to www.OpenBequest.org</div>
        <div class="light">In 20 minutes you can have a</div>
        <div class="strong">legal will – for free.</div>
      </div>
      <div class="abs contact-pill">CONTACT US</div>
      <div class="abs questions"><h3>Have more questions?</h3><p>Please contact us at Harborline and<br>Caring Works</p></div>
      <div class="abs contact-row" style="top:616px"><span class="ring"><svg width="16" height="18" viewBox="0 0 16 18"><path d="M8 17s-6-6-6-10a6 6 0 0 1 12 0c0 4-6 10-6 10z" fill="none" stroke="#fff" stroke-width="1.3"/><circle cx="8" cy="7" r="2.2" fill="none" stroke="#fff" stroke-width="1.3"/></svg></span><span>2150 Alder Ridge Rd., Suite 6<br>Fargo, ND&nbsp; 58102</span></div>
      <div class="abs contact-row" style="top:659px"><span class="ring"><svg width="12" height="18" viewBox="0 0 12 18"><rect x="1" y="1" width="10" height="16" rx="2" fill="none" stroke="#fff" stroke-width="1.3"/><path d="M4.5 14h3" stroke="#fff" stroke-width="1.3"/></svg></span><span>Call us Today!<br><b>701-555-0184</b> (ext. 100)</span></div>
      <div class="abs contact-row" style="top:702px"><span class="ring"><svg width="18" height="18" viewBox="0 0 18 18"><circle cx="9" cy="9" r="7.5" fill="none" stroke="#fff" stroke-width="1.2"/><ellipse cx="9" cy="9" rx="3.2" ry="7.5" fill="none" stroke="#fff" stroke-width="1.2"/><path d="M1.5 9h15" stroke="#fff" stroke-width="1.2"/></svg></span><span>mwalden@harborlinecw.org<br><b>www.harborlinecw.org</b></span></div>
      <div class="abs follow">Follow us <i></i></div>
      <p class="abs fineprint">This material has been prepared for general informational purposes only and is not meant to provide tax, accounting or legal advice. Harborline and Caring Works is not a professional advisory firm. Please consult with your own tax or financial professional before making any decision about Smart Giving.</p>
    </div>

    <div class="abs cover">
      <svg class="abs" style="left:0;top:0" width="370" height="838" viewBox="0 0 370 838">
        <defs><linearGradient id="field" x1="0" y1="0" x2="0" y2="1"><stop offset="0" stop-color="#8fa86a"/><stop offset=".5" stop-color="#5d7f3e"/><stop offset="1" stop-color="#3c5a2b"/></linearGradient></defs>
        <rect width="370" height="692" fill="var(--navy)"/>
        <path d="M0 0H370V272 Q185 362 0 272Z" fill="url(#field)" role="img" aria-label="Photo of a smiling young man in a cap leaning on a garden tool in a green field"/>
        <path d="M0 272 Q185 362 370 272 Q185 346 0 290Z" fill="var(--green)"/>
        <path d="M0 700 Q185 600 370 700 V838 H0Z" fill="#fff"/>
        <path d="M0 690 Q185 588 370 690 Q185 612 0 705Z" fill="var(--green)"/>
      </svg>
      <div class="abs cover-text">
        <div class="cover-kicker">Transform Your Giving</div>
        <div class="cover-line"><svg viewBox="0 0 34 34"><circle cx="17" cy="17" r="15" fill="none" stroke="#4cb848" stroke-width="3"/><path d="M10 17l5 5 10-10" fill="none" stroke="#4cb848" stroke-width="3"/></svg><span>Be <span class="accent">Strategic</span></span></div>
        <div class="cover-line"><svg viewBox="0 0 34 34"><circle cx="17" cy="17" r="15" fill="none" stroke="#4cb848" stroke-width="3"/><path d="M10 17l5 5 10-10" fill="none" stroke="#4cb848" stroke-width="3"/></svg><span>Be <span class="accent">Smart</span></span></div>
        <p class="cover-tag">Discover the impact of Smart Giving with<br>Harborline and Caring Works</p>
      </div>
      <div class="abs method-row">
        <div class="method" style="margin-top:18px"><div class="ring"><svg viewBox="0 0 30 30"><circle cx="15" cy="15" r="11" fill="none" stroke="#fff" stroke-width="1.5"/><text x="15" y="20" text-anchor="middle" font-size="14" font-weight="700" fill="#fff" font-family="Montserrat,sans-serif">B</text></svg></div>Crypto</div>
        <div class="method" style="margin-top:5px"><div class="ring"><svg viewBox="0 0 30 30"><path d="M4 11L15 5l11 6z M5 24h20 M7 12v10 M12 12v10 M18 12v10 M23 12v10" fill="none" stroke="#fff" stroke-width="1.5"/></svg></div>DAF's</div>
        <div class="method"><div class="ring"><svg viewBox="0 0 30 30"><path d="M4 25h22 M6 25v-7h4v7 M12 25V14h4v11 M18 25V17h4v8 M5 14l6-5 5 3 8-6" fill="none" stroke="#fff" stroke-width="1.5"/></svg></div>Stocks<br>&amp; Securities</div>
        <div class="method" style="margin-top:5px"><div class="ring"><svg viewBox="0 0 30 30"><rect x="6" y="13" width="18" height="12" fill="none" stroke="#fff" stroke-width="1.5"/><rect x="4" y="9" width="22" height="4" fill="none" stroke="#fff" stroke-width="1.5"/><path d="M15 9v16 M15 9c-3-5-7-3-5 0 M15 9c3-5 7-3 5 0" fill="none" stroke="#fff" stroke-width="1.5"/></svg></div>QCDs</div>
        <div class="method" style="margin-top:18px"><div class="ring"><svg viewBox="0 0 30 30"><circle cx="13" cy="15" r="9" fill="none" stroke="#fff" stroke-width="1.5"/><path d="M13 9v6l3 2 M11 4h4" fill="none" stroke="#fff" stroke-width="1.5"/><circle cx="22" cy="22" r="5" fill="var(--navy)" stroke="#fff" stroke-width="1.5"/></svg></div>Charitable<br>Annuity</div>
      </div>
      <div class="abs wordmark-dark"><div class="name"><span class="dot"></span>Harborline</div><div class="sub">HARBORLINE AND CARING WORKS, INC.</div></div>
    </div>
  </section>

  <!-- ============ INSIDE ============ -->
  <section class="sheet sheet--inside">
    <div class="abs fold" style="left:353px"></div>
    <div class="abs fold" style="left:707px"></div>

    <svg class="abs hero-photo" viewBox="0 0 1077 240">
      <defs><linearGradient id="drive" x1="0" y1="0" x2="1" y2="0"><stop offset="0" stop-color="#a9b6a4"/><stop offset=".5" stop-color="#6f8c6a"/><stop offset="1" stop-color="#5a7a3e"/></linearGradient></defs>
      <path d="M170 0H910 Q830 150 560 168 Q330 182 170 0Z" fill="url(#drive)" role="img" aria-label="Photo of a smiling older man driving a light blue convertible along a green countryside road"/>
      <path d="M120 0 Q320 220 740 160 Q320 230 100 0Z" fill="#fff"/>
      <path d="M300 130 Q520 230 740 160 Q520 212 300 130Z" fill="var(--green)"/>
    </svg>

    <div class="abs title-badge"><span class="num">5</span><span class="words">STRATEGIC<br>AND SMART<br>WAYS TO GIVE</span></div>
    <svg class="abs" style="left:90px;top:130px" width="24" height="16"><path d="M0 0h24L6 16z" fill="var(--navy)"/></svg>

    <!-- column 1 -->
    <div class="column" style="left:29px;top:164px;width:322px">
      <div class="way">
        <div class="icon" style="left:0;top:0"><svg viewBox="0 0 52 52"><path d="M8 44h36 M10 44V32h6v12 M20 44V24h6v20 M30 44V30h6v14 M38 44V20h6v24 M11 26l10-10 9 8 12-12" fill="none" stroke="#fff" stroke-width="2"/><circle cx="21" cy="16" r="2" fill="#fff"/><circle cx="30" cy="24" r="2" fill="#fff"/><circle cx="42" cy="12" r="2" fill="#fff"/></svg></div>
        <div class="head"><h2>Gifts of Stocks or Appreciated Assets</h2><p class="lead">Consider long-term publicly traded stock as a way to give to your favorite charity.</p></div>
        <p class="body-copy" style="margin-top:8px">Make a significantly bigger impact when you donate long-term appreciated securities, including stock, mutual funds and bonds directly to your favorite charity.</p>
        <span class="how">How Does It Work?</span>
        <p class="body-copy">When you donate an appreciated asset to a charity you generally take a tax deduction for the full market value. Your contribution and tax deduction may be significantly higher than contributing after tax proceeds.</p>
      </div>
      <div class="way">
        <div class="icon" style="left:0;top:0"><svg viewBox="0 0 52 52"><path d="M6 18L26 8l20 10z M8 44h36 M8 40h36 M12 20v18 M20 20v18 M32 20v18 M40 20v18" fill="none" stroke="#fff" stroke-width="2"/><circle cx="26" cy="14" r="2" fill="#fff"/></svg></div>
        <div class="head"><h2>Donor-Advised<br>Fund (DAF)</h2><p class="lead" style="margin-top:2px">Consider a<br>DAF - a tax-advantageous way to give to your favorite charity.</p></div>
        <p class="body-copy" style="margin-top:8px">A Donor-Advised Fund is an investment account for supporting your favorite charities.</p>
        <span class="how">How Does It Work?</span>
        <p class="body-copy">You contribute cash, stocks, crypto, non-publicly traded assets and private company stock for an immediate taxdeduction. You recommend grants be made from your DAF to your favorite charity.</p>
      </div>
    </div>

    <!-- column 2 -->
    <div class="column" style="left:378px;top:252px;width:325px">
      <div class="way">
        <div class="icon" style="left:0;top:0"><svg viewBox="0 0 52 52"><circle cx="26" cy="26" r="19" fill="none" stroke="#fff" stroke-width="2"/><circle cx="26" cy="26" r="14" fill="none" stroke="#fff" stroke-width="1.5"/><text x="26" y="33" text-anchor="middle" font-size="20" font-weight="700" fill="#fff" font-family="Montserrat,sans-serif">B</text></svg></div>
        <div class="head"><h2>Cryptocurrency</h2><p class="lead" style="margin-top:10px">Consider donating Bitcoin and other cryptocurrencies to your favorite charity.</p></div>
        <p class="body-copy" style="margin-top:12px">Bitcoin and other cryptocurrencies can be donated to charity like other appreciated assets.</p>
        <span class="how">How Does It Work?</span>
        <p class="body-copy" style="margin-bottom:16px">Donors find it useful to open a Donor-Advised Fund. This provides two significant benefits for you and your favorite charity:</p>
        <ul class="ticks body-copy">
          <li><svg viewBox="0 0 16 16"><circle cx="8" cy="8" r="6.5" fill="none" stroke="#4cb848" stroke-width="1.4"/><path d="M5 8.2l2 2 4-4.2" fill="none" stroke="#4cb848" stroke-width="1.4"/></svg>Your tax deduction will be equal to the appraised market value of the crypto.</li>
          <li><svg viewBox="0 0 16 16"><circle cx="8" cy="8" r="6.5" fill="none" stroke="#4cb848" stroke-width="1.4"/><path d="M5 8.2l2 2 4-4.2" fill="none" stroke="#4cb848" stroke-width="1.4"/></svg>Your donation is tax-smart because it may eliminate capital gains taxes AND your favorite charity will receive 100% of the value of the contribution.</li>
        </ul>
        <p class="body-copy">Often charities are not able to accept direct donations of bitcoin/crypto so using a DAF is a great way to donate these assets.</p>
      </div>
    </div>
    <svg class="abs" style="left:288px;top:742px" width="510" height="96" viewBox="0 0 510 96"><path d="M0 96 Q250 -20 510 96Z" fill="var(--navy)"/><path d="M30 86 Q250 -30 480 86 Q250 -10 30 86Z" fill="var(--green)"/></svg>

    <!-- column 3 -->
    <div class="column" style="left:736px;top:92px;width:330px">
      <div class="way">
        <div class="icon" style="left:0;top:0"><svg viewBox="0 0 52 52"><rect x="10" y="24" width="32" height="20" fill="none" stroke="#fff" stroke-width="2"/><rect x="7" y="17" width="38" height="7" fill="none" stroke="#fff" stroke-width="2"/><path d="M26 17v27 M26 17c-5-9-13-6-9 0 M26 17c5-9 13-6 9 0" fill="none" stroke="#fff" stroke-width="2"/></svg></div>
        <div class="head"><h2>Qualified Charitable Distributions (QCDs)</h2><p class="lead">Consider a QCD – when planning your IRA withdrawal strategy...and donate to your favorite charity.</p></div>
        <p class="body-copy" style="margin-top:10px">IRA owners over age 70 1/2 can transfer dollars from an IRA to charity tax-free each year.</p>
        <span class="how">How Does It Work?</span>
        <p class="body-copy">Are you 72 and required to take a minimum distribution (RMD) from your IRA but do not need the funds? Consider a Qualified Charitable Distribution. A QCD is tax-free when paid directly from your IRA to your favorite eligible charity. Allow time to complete this transaction before year's end.</p>
      </div>
      <div class="way">
        <div class="icon" style="left:0;top:0"><svg viewBox="0 0 52 52"><circle cx="22" cy="26" r="15" fill="none" stroke="#fff" stroke-width="2"/><path d="M22 16v10l5 4 M18 7h8" fill="none" stroke="#fff" stroke-width="2"/><circle cx="35" cy="36" r="8" fill="var(--navy)" stroke="#fff" stroke-width="2"/><text x="35" y="40.5" text-anchor="middle" font-size="12" font-weight="700" fill="#fff" font-family="Montserrat,sans-serif">$</text></svg></div>
        <div class="head"><h2>Charitable Gift<br>Annuity</h2><p class="lead" style="margin-top:6px">Consider establishing a Charitable Gift Annuity</p></div>
        <p class="body-copy" style="margin-top:4px">You make a donation to a single charity. The gift is set aside in a reserve account and invested.</p>
        <span class="how">How Does It Work?</span>
        <p class="body-copy">A Charitable Gift Annuity is a contract between you and a charity. You make a sizeable gift using various assets. The money is invested, and you become eligible to take a partial tax deduction. You (and your spouse if done as a couple) receive a fixed stream of income. At the end of your life the charity receives the remainder of the gift.</p>
      </div>
    </div>
  </section>

</div>
</body>
</html>
```